Mental Health & Addiction Podcast Art

Project: Podcast Cover Art / Visual Identity
Podcast Name: The Renewal Compass
Focus: Recovery from substance use and mental health
Objectives
Create compelling podcast artwork that:
Reflects the themes of hope, healing, and personal growth
Establishes credibility and professionalism
Appeals to individuals seeking recovery resources and support
Maintains strong brand consistency with Harborline Wellness
Brand Integration Requirements
Logo incorporation: Integrate an element from the Harborline Wellness Logo—potentially an abstract or partial use of the sun motif
Flexibility: Open to creative interpretations (e.g., sun rays as background texture, sunrise gradient, partial sun as a design accent)
Mandatory: Must adhere to existing Harborline Wellness brand guidelines (approved color palette, typography, and visual style)

Target Market(s)

United states, people with addiction and mental health disorders.

Industry/Entity Type

Wellness

Font styles to use
Other font styles liked:
• See Brand Guide

Requirements
Must have
• Match brand guide, in corporate elements of the Harborline Wellness Logo icon

```html
<!DOCTYPE html>
<html lang="en">
<head>
<meta charset="utf-8">
<title>The Renewal Compass – Podcast Cover Art</title>
<link rel="stylesheet" href="https://fonts.googleapis.com/css2?family=DM+Serif+Display:ital@0;1&family=IBM+Plex+Sans:wght@300;400;700&display=swap">
<style>
  :root {
    --navy: #0b4866;
    --navy-deep: #073d58;
    --navy-light: #2c6784;
    --amber: #fcad00;
    --white: #ffffff;
    --page: #ffffff;
    --serif: "DM Serif Display", Georgia, serif;
    --sans: "IBM Plex Sans", Arial, sans-serif;
  }
  * { margin: 0; padding: 0; box-sizing: border-box; }
  html, body { width: 1200px; height: 611px; overflow: hidden; background: var(--page); }
  .canvas { position: relative; width: 1200px; height: 611px; }

  .cover {
    position: absolute; top: 22px;
    width: 570px; height: 570px;
    background: var(--navy);
    overflow: hidden;
    color: var(--white);
  }
  .cover--bold { left: 19px; }
  .cover--minimal { left: 609px; }

  /* Bold cover */
  .sun-accent {
    position: absolute; left: 0; top: 0; width: 570px; height: 350px;
    background: radial-gradient(ellipse 70% 80% at 50% 35%, var(--amber) 0%, rgba(252,173,0,0.85) 35%, rgba(252,173,0,0.25) 70%, rgba(11,72,102,0) 100%);
  }
  .bold-title {
    position: absolute; left: 0; top: 258px; width: 570px;
    font-family: var(--serif); font-style: italic; font-weight: 400;
    font-size: 74px; line-height: 64px; text-align: center;
    letter-spacing: -0.5px;
  }
  .bold-title span { display: block; }
  .tagline-pill {
    position: absolute; left: 50%; top: 467px; transform: translateX(-50%);
    height: 25px; padding: 0 10px;
    background: var(--amber); color: var(--navy-deep);
    border-radius: 13px;
    font-family: var(--sans); font-weight: 300; font-size: 14px;
    line-height: 25px; white-space: nowrap;
  }
  .brand {
    position: absolute; display: flex; align-items: center; gap: 5px;
    font-family: var(--sans); font-weight: 400; text-transform: uppercase;
    color: var(--white); white-space: nowrap;
  }
  .brand-dot { border: 1.5px solid var(--white); border-radius: 50%; }
  .cover--bold .brand { left: 50%; top: 513px; transform: translateX(-50%); font-size: 13px; }
  .cover--bold .brand-dot { width: 20px; height: 20px; }

  /* Minimal cover */
  .glow-accent {
    position: absolute; left: 150px; top: 0; width: 420px; height: 300px;
    background: radial-gradient(ellipse 80% 90% at 85% 25%, rgba(44,103,132,0.75) 0%, rgba(44,103,132,0.3) 55%, rgba(11,72,102,0) 100%);
  }
  .minimal-title { position: absolute; left: 34px; top: 248px; }
  .minimal-title .word-small {
    display: block; font-family: var(--sans); font-weight: 300;
    font-size: 60px; line-height: 60px; letter-spacing: 1px;
  }
  .minimal-title .word-large {
    display: block; font-family: var(--serif); font-style: italic;
    color: var(--amber); font-size: 96px; line-height: 84px;
    margin-left: -2px; letter-spacing: -1px;
  }
  .minimal-title .word-base { font-size: 72px; line-height: 78px; }
  .tagline-bar {
    position: absolute; left: 41px; top: 491px;
    border-left: 3px solid var(--amber);
    padding-left: 12px;
    font-family: var(--sans); font-weight: 300; font-size: 15px; line-height: 19px;
  }
  .tagline-bar strong { font-weight: 700; }
  .cover--minimal .brand { left: 412px; top: 510px; font-size: 9px; gap: 3px; }
  .cover--minimal .brand-dot { width: 14px; height: 14px; }
</style>
</head>
<body>
<main class="canvas">

  <section class="cover cover--bold" aria-label="The Renewal Compass cover, bold version">
    <div class="sun-accent" role="img" aria-label="Large amber sun motif with radiating rays"></div>
    <h1 class="bold-title"><span>The</span><span>Renewal</span><span>Compass</span></h1>
    <p class="tagline-pill">Recovery from substance use and mental health</p>
    <div class="brand"><span class="brand-dot"></span>Harborline Wellness</div>
  </section>

  <section class="cover cover--minimal" aria-label="The Renewal Compass cover, minimal version">
    <div class="glow-accent" role="img" aria-label="Faint partial sun rays over patterned background"></div>
    <h2 class="minimal-title">
      <span class="word-small">THE</span>
      <span class="word-large">Renewal</span>
      <span class="word-small word-base">COMPASS</span>
    </h2>
    <p class="tagline-bar"><strong>Recovery</strong> from substance use<br>and mental health</p>
    <div class="brand"><span class="brand-dot"></span>Harborline Wellness</div>
  </section>

</main>
</body>
</html>
```